当社 ㈱セキレイワークスの年賀状(デザイン面のみ)です。
400枚余りをクライアントや雑誌社等の媒体、広告代理店、印刷会社など取引先に送ります。ハガキサイズ(148×100㎜)。特色2色刷。デザインは自由です。あくまで参考ですが、これまでの年賀状の抜粋を添付します。加えて当社のロゴデータを添付します。
明けましておめでとうございます。
創業以来四半世紀に及ぶ活動を礎に、また新たな第一歩を踏み出しました。
これからも、アグレッシブに、元気に、正しきことに労を惜しまず、日々
挑戦し続けます。本年も更に皆様のお役に立てる存在を目指し精進致します。
株式会社セキレイワークス
代表取締役会長 ●●●● 代表取締役社長 ●●●● 社員一同

※基本的に上記の挨拶文を入れていただきますが、これを入れない案(過去年賀状をご参照)もOKです。(その場合、挨拶文はポスト面に入れます。ポスト面のデザインは不要です。)
当社ホームページ
http://www.sekirei-works.example/

ファッションの広告宣伝を取り扱うという当社の業務内容を意識して頂いたこと。
これまでの当社の年賀状と少し違った見え方のデザイン。
巧みな2色での表現。
デザインが上品でまとまっていること。
これらの理由から選択させて頂きました。

この度は多くのご提案を頂きましてありがとうございました。
どの案も素晴らしく、それぞれ個性のある提案であったため、決定に時間が掛かってしまったことをお詫びします。
また、別案件でご相談させて頂く際はよろしくお願いいたします。

```html
<!DOCTYPE html>
<html lang="ja">
<head>
<meta charset="utf-8">
<title>年賀状 2014 — 株式会社セキレイワークス</title>
<link rel="stylesheet" href="https://fonts.googleapis.com/css2?family=Noto+Serif+JP:wght@400;700&display=swap">
<style>
  :root {
    --paper: #ffffff;
    --ink: #1a1a1a;
    --gold-deep: #a8730c;
    --gold: #d9a33a;
    --gold-light: #f3d894;
    --gold-pale: #fbefd2;
    --horse-blue: #bcd3e2;
    --horse-blue-light: #dde9f1;
  }
  * { margin: 0; padding: 0; box-sizing: border-box; }
  html, body {
    width: 839px; height: 1200px; overflow: hidden;
    background: var(--paper);
  }
  .card {
    position: relative;
    width: 839px; height: 1200px;
    background: var(--paper);
    font-family: "Noto Serif JP", serif;
    color: var(--ink);
    overflow: hidden;
  }
  .gold-waves {
    position: absolute; left: 0; top: 0; width: 100%; height: 320px;
    background:
      linear-gradient(160deg, rgba(255,255,255,0) 38%, rgba(251,239,210,0.75) 48%, rgba(255,255,255,0) 58%),
      linear-gradient(200deg, rgba(255,255,255,0) 55%, rgba(168,115,12,0.45) 68%, rgba(255,255,255,0) 80%),
      linear-gradient(180deg, var(--gold-deep) 0%, var(--gold) 30%, var(--gold-light) 62%, var(--gold-pale) 82%, rgba(255,255,255,0) 100%);
  }
  .horse-figure {
    position: absolute; left: 262px; top: 585px; width: 420px; height: 430px;
    border-radius: 46% 40% 42% 38%;
    background: radial-gradient(ellipse 60% 55% at 50% 45%, var(--horse-blue) 0%, var(--horse-blue-light) 65%, rgba(221,233,241,0.4) 100%);
  }
  .greeting__title {
    position: absolute; left: 0; top: 262px; width: 100%;
    text-align: center;
    font-size: 34px; font-weight: 700; letter-spacing: 0.04em; line-height: 50px;
  }
  .greeting__body {
    position: absolute; left: 0; top: 343px; width: 100%;
    text-align: center;
    font-size: 24px; line-height: 41px; letter-spacing: 0.02em;
  }
  .signature {
    position: absolute; left: 0; top: 590px; width: 100%;
    text-align: center;
  }
  .signature__company {
    font-size: 30px; font-weight: 700; line-height: 42px;
  }
  .signature__line {
    font-size: 27px; line-height: 40px;
  }
  .signature__date {
    position: absolute; left: 590px; top: 740px;
    font-size: 20px; letter-spacing: 0.04em;
  }
  .brand {
    position: absolute; left: 0; top: 978px; width: 100%;
    text-align: center;
    font-size: 36px; font-weight: 400; letter-spacing: 0.03em;
    color: var(--ink);
  }
</style>
</head>
<body>
  <main class="card">
    <div class="gold-waves" role="img" aria-label="金色の波が重なる抽象的な背景模様"></div>
    <div class="horse-figure" role="img" aria-label="淡い水色で描かれた駆ける馬のシルエット"></div>

    <h1 class="greeting__title">明けましておめでとうございます。</h1>
    <p class="greeting__body">
      創業以来四半世紀に及ぶ活動を礎に、また新たな<br>
      第一歩を踏み出しました。<br>
      これからも、アグレッシブに、元気に、正しきことに<br>
      労を惜しまず、日々挑戦し続けます。<br>
      本年も更に皆様のお役に立てる<br>
      存在を目指し精進致します。
    </p>

    <section class="signature">
      <p class="signature__company">株式会社セキレイワークス</p>
      <p class="signature__line">代表取締役会長 ●●●●</p>
      <p class="signature__line">代表取締役社長 ●●●●</p>
      <p class="signature__line">社員一同</p>
    </section>
    <p class="signature__date">2014.1.1</p>

    <p class="brand">SEKIREI WORKS INC.</p>
  </main>
</body>
</html>
```